Ferris Contracting LLC Business Card Design

I am looking for a creative and unique business card design. We are a commercial construction general contractor. With the name "FERRIS" Contracting, I am hoping to see some neat designs that correlate with the name.

```html
<!DOCTYPE html>
<html lang="en">
<head>
<meta charset="utf-8">
<title>Ferris Contracting LLC – Business Card</title>
<link rel="stylesheet" href="https://fonts.googleapis.com/css2?family=Arimo:wght@400;700&family=Oswald:wght@500&family=Saira+Semi+Condensed:wght@600&display=swap">
<style>
  :root {
    --page-bg: #7c7c7c;
    --card-edge: #c9c9cc;
    --card-dark: #0b0b0c;
    --card-mid: #3a3b3d;
    --brand-blue: #1a8fe6;
    --brand-blue-light: #36c2ff;
    --text-white: #f2f2f2;
    --text-soft: #d9d9d9;
  }
  * { box-sizing: border-box; margin: 0; padding: 0; }
  html, body { width: 1200px; height: 1200px; overflow: hidden; }
  body {
    background: var(--page-bg);
    font-family: "Arimo", Arial, sans-serif;
    position: relative;
  }
  .card {
    position: absolute;
    left: 176px;
    width: 850px;
    height: 536px;
    border-radius: 40px;
    background: var(--card-edge);
    padding: 16px;
  }
  .card--front { top: 41px; }
  .card--back { top: 621px; }
  .card__face {
    position: relative;
    width: 100%;
    height: 100%;
    border-radius: 28px;
    overflow: hidden;
    background: radial-gradient(ellipse 60% 55% at 55% 45%, var(--card-mid) 0%, #1a1b1c 55%, var(--card-dark) 100%);
  }

  /* Front */
  .brand-name {
    position: absolute;
    left: 0; right: 0;
    top: 160px;
    text-align: center;
    color: var(--brand-blue);
    font-weight: 700;
    line-height: 1;
  }
  .brand-name__main { display: block; font-size: 96px; letter-spacing: 2px; }
  .brand-name__sub { display: block; font-size: 34px; letter-spacing: 8px; margin-top: 10px; }
  .front-rule {
    position: absolute;
    left: 0; right: 0;
    top: 412px;
    height: 2px;
    background: var(--brand-blue);
  }
  .website {
    position: absolute;
    left: 0; right: 0;
    top: 440px;
    display: flex;
    justify-content: center;
    align-items: center;
    gap: 26px;
    font-family: "Oswald", "Arial Narrow", sans-serif;
    font-weight: 500;
    font-size: 26px;
    color: var(--text-white);
    letter-spacing: 1px;
  }
  .website__accent { color: var(--brand-blue); }
  .website__bars { display: flex; gap: 4px; }
  .website__bars span { width: 4px; height: 34px; background: var(--text-soft); }
  .website__bars span.is-blue { width: 6px; background: var(--brand-blue); }

  /* Back */
  .company {
    position: absolute;
    right: 54px;
    top: 92px;
    text-align: right;
  }
  .company__name { font-size: 34px; font-weight: 400; color: var(--text-white); letter-spacing: 0.5px; }
  .company__tagline { font-size: 21px; color: var(--brand-blue); margin-top: 8px; }
  .contact-list {
    position: absolute;
    left: 350px;
    top: 190px;
    width: 432px;
  }
  .contact-row {
    position: relative;
    height: 78px;
    display: flex;
    align-items: center;
    border-bottom: 2px solid var(--brand-blue);
  }
  .contact-row:last-child { border-bottom: none; }
  .contact-row__text {
    width: 350px;
    text-align: right;
    padding-right: 14px;
    color: var(--text-white);
    font-size: 22px;
  }
  .contact-row__text--phone {
    font-family: "Saira Semi Condensed", Arial, sans-serif;
    font-weight: 600;
    font-size: 38px;
    letter-spacing: 1px;
  }
  .contact-row__icon {
    width: 82px;
    height: 100%;
    display: flex;
    align-items: center;
    justify-content: center;
    border-left: 2px solid var(--brand-blue);
  }
  .contact-list__rule-top {
    position: absolute;
    left: 350px;
    top: 168px;
    width: 2px;
    height: 22px;
    background: var(--brand-blue);
    margin-left: 350px;
  }
  .back-band {
    position: absolute;
    left: 0; bottom: 0;
    width: 100%;
    height: 80px;
  }
</style>
</head>
<body>

<section class="card card--front" aria-label="Business card front">
  <div class="card__face">
    <h1 class="brand-name">
      <span class="brand-name__main">FERRIS</span>
      <span class="brand-name__sub">CONTRACTING</span>
    </h1>
    <div class="front-rule"></div>
    <div class="website">
      <div class="website__bars"><span></span><span class="is-blue"></span><span></span></div>
      <span>WWW.<span class="website__accent">FERRIS</span>CONTRACTING.COM</span>
      <div class="website__bars"><span></span><span class="is-blue"></span><span></span></div>
    </div>
  </div>
</section>

<section class="card card--back" aria-label="Business card back">
  <div class="card__face">
    <div class="company">
      <h2 class="company__name">FERRIS CONTRACTING</h2>
      <p class="company__tagline">Commercial Construction</p>
    </div>

    <div class="contact-list">
      <div class="contact-row">
        <p class="contact-row__text contact-row__text--phone">00 1 23456789</p>
        <div class="contact-row__icon">
          <svg width="52" height="52" viewBox="0 0 52 52" aria-hidden="true">
            <circle cx="26" cy="26" r="24" fill="none" stroke="var(--brand-blue)" stroke-width="2"/>
            <rect x="19" y="13" width="14" height="26" rx="3" fill="none" stroke="var(--brand-blue)" stroke-width="2"/>
            <line x1="24" y1="35" x2="28" y2="35" stroke="var(--brand-blue)" stroke-width="2"/>
          </svg>
        </div>
      </div>
      <div class="contact-row">
        <p class="contact-row__text">info@ferriscontracting.com</p>
        <div class="contact-row__icon">
          <svg width="52" height="52" viewBox="0 0 52 52" aria-hidden="true">
            <circle cx="26" cy="26" r="24" fill="none" stroke="var(--brand-blue)" stroke-width="2"/>
            <rect x="14" y="18" width="24" height="16" fill="none" stroke="var(--brand-blue)" stroke-width="2"/>
            <polyline points="14,18 26,28 38,18" fill="none" stroke="var(--brand-blue)" stroke-width="2"/>
          </svg>
        </div>
      </div>
      <div class="contact-row">
        <p class="contact-row__text">USA, ABC Street, xxx Building</p>
        <div class="contact-row__icon">
          <svg width="52" height="52" viewBox="0 0 52 52" aria-hidden="true">
            <circle cx="26" cy="26" r="24" fill="none" stroke="var(--brand-blue)" stroke-width="2"/>
            <path d="M26 38 C20 31 17 27 17 22 A9 9 0 0 1 35 22 C35 27 32 31 26 38 Z" fill="var(--brand-blue)"/>
            <circle cx="26" cy="22" r="3.5" fill="var(--card-dark)"/>
          </svg>
        </div>
      </div>
    </div>

    <svg class="back-band" viewBox="0 0 818 80" preserveAspectRatio="none" aria-hidden="true">
      <defs>
        <linearGradient id="bandBlue" x1="0" y1="0" x2="1" y2="0">
          <stop offset="0" stop-color="var(--brand-blue)"/>
          <stop offset="0.4" stop-color="var(--brand-blue-light)"/>
          <stop offset="1" stop-color="var(--brand-blue)"/>
        </linearGradient>
      </defs>
      <path d="M0 24 L120 24 C170 24 200 40 230 52 L818 52 L818 80 L0 80 Z" fill="url(#bandBlue)"/>
    </svg>
  </div>
</section>

</body>
</html>
```